FUNDRAISER FLYER For Tshirt Business

I would like a front and back flyer advertising fundraising for my print on demand business(SHIRTS AT BRIM) I would like an eye catching color scheme. I don't want it to be cluttered the font should be bold. I am attaching a list of things I need included, please use this as informational that I need on the flyer but not for direction and style. Quick turnaround time. Please add our Instagram and FB info to Flyer with Contact Info

Target Market(s)

Organizations looking to add to their capital by doing fundraising.

Industry/Entity Type

Organization

Requirements
Must have
• Information provided make sure the packages is easily defined
Nice to have
• A key information
Should not have
• Do not copy the images provided. I didn’t not like this layout.

```html
<!DOCTYPE html>
<html lang="en">
<head>
<meta charset="utf-8">
<title>Shirts At Brim – Fundraiser Flyer</title>
<link href="https://fonts.googleapis.com/css2?family=Oswald:wght@400;500;700&family=Rubik:wght@900&family=Titan+One&display=swap" rel="stylesheet">
<style>
  :root{
    --red:#ec2028;
    --yellow:#fcbf12;
    --black:#050505;
    --white:#ffffff;
    --dot:#d9d9d9;
    --stage:#a8a8a8;
    --shirt-a:#f2f2f4;
    --shirt-b:#dcdce0;
  }
  *{margin:0;padding:0;box-sizing:border-box}
  html,body{width:1200px;height:960px;overflow:hidden;background:var(--stage)}
  .canvas{position:relative;width:1200px;height:960px}
  .page{position:absolute;background:var(--white);overflow:hidden}
  .page--front{left:62px;top:122px;width:506px;height:716px}
  .page--back{left:628px;top:119px;width:511px;height:721px}
  .abs{position:absolute}
  svg.abs{overflow:visible}

  /* front */
  .headline{left:27px;top:44px;font-family:"Rubik",sans-serif;font-weight:900;font-size:31px;line-height:35px;color:var(--black);letter-spacing:.3px}
  .brand{display:flex;align-items:center;gap:6px;font-family:"Oswald",sans-serif;font-weight:500;font-size:18px;color:var(--red);letter-spacing:.5px;white-space:nowrap}
  .brand__dot{width:12px;height:12px;border-radius:50%;background:var(--red)}
  .brand--front{left:352px;top:58px}
  .dots{display:grid;gap:0}
  .dots span{width:14px;height:14px;display:flex;align-items:center;justify-content:center}
  .dots span::after{content:"";width:5px;height:5px;border-radius:50%;background:var(--dot)}
  .shirt-photo{left:26px;width:122px;height:109px;background:linear-gradient(160deg,var(--shirt-a),var(--shirt-b));box-shadow:0 3px 0 #9c9c9c}
  .package{left:169px;width:297px;height:109px;padding:12px 0 0 25px;font-family:"Oswald",sans-serif;font-weight:400;font-size:13.5px;line-height:14.7px;color:var(--white);box-shadow:0 3px 0 #b5b5b5}
  .package--red{background:var(--red)}
  .package--yellow{background:var(--yellow);color:var(--black)}
  .package--black{background:var(--black)}
  .contact-title{left:19px;top:636px;font-family:"Oswald",sans-serif;font-weight:700;font-size:16px;color:var(--white)}
  .contact-body{left:19px;top:658px;width:170px;font-family:"Oswald",sans-serif;font-weight:400;font-size:12.5px;line-height:16.5px;color:var(--white)}
  .phone{left:258px;top:632px;font-family:"Rubik",sans-serif;font-weight:900;font-size:25px;letter-spacing:1.5px;color:var(--black)}
  .contact-line{left:258px;display:flex;align-items:center;gap:7px;font-family:"Oswald",sans-serif;font-size:13.5px;color:var(--black)}

  /* back */
  .benefits-title{left:140px;top:24px;width:225px;text-align:center;font-family:"Oswald",sans-serif;font-weight:700;font-size:62px;line-height:74px;color:var(--yellow);text-shadow:2px 2px 0 var(--black);letter-spacing:-1px}
  .benefit-list{left:101px;top:102px;width:330px;list-style:none;font-family:"Oswald",sans-serif;font-weight:500;font-size:12.3px;line-height:16.5px;color:var(--black);text-transform:uppercase}
  .brand--back{left:218px;top:432px;font-size:14px}
  .promise{left:126px;top:474px;width:260px;height:198px;border:1px dashed #444}
  .promise__line{position:absolute;left:-6px;width:272px;text-align:center;font-family:"Titan One",sans-serif;white-space:nowrap}
  .promise__line--outline{color:var(--white);-webkit-text-stroke:1.6px var(--black);font-size:31px;letter-spacing:1px}
  .promise__line--red{color:var(--red);font-size:30px}
  .promise__line--big{color:var(--yellow);font-size:68px;letter-spacing:2px}
</style>
</head>
<body>
<main class="canvas">

  <section class="page page--front" aria-label="Front of fundraiser flyer">
    <svg class="abs" style="left:0;top:0" width="330" height="175" viewBox="0 0 330 175" aria-hidden="true">
      <polygon fill="var(--yellow)" points="0,36 30,30 48,22 90,24 140,16 200,18 260,10 320,12 314,140 290,146 250,152 200,150 150,162 100,166 40,160 0,156"/>
      <polyline fill="none" stroke="var(--black)" stroke-width="1.4" points="320,12 314,140 290,146 250,152 200,150 150,162 100,166 40,160 0,156"/>
    </svg>
    <h1 class="abs headline">BUILD YOUR<br>TSHIRT STORE<br>FUNDARISER</h1>

    <div class="abs brand brand--front"><span class="brand__dot"></span>SHIRTS AT BRIM</div>

    <div class="abs dots" style="left:402px;top:133px;grid-template-columns:repeat(7,14px)">
      <span></span><span></span><span></span><span></span><span></span><span></span><span></span>
      <span></span><span></span><span></span><span></span><span></span><span></span><span></span>
      <span></span><span></span><span></span><span></span><span></span><span></span><span></span>
    </div>

    <div class="abs shirt-photo" style="top:192px" role="img" aria-label="Photo of a white t-shirt with the store name printed on the chest"></div>
    <div class="abs package package--red" style="top:190px">
      • 2 Shirt choice<br>• 1 Design<br>• 1 Color<br>Sell: 1-25 earn 20%<br>25-50 earn 25%<br>50-100 earn 30%
    </div>

    <div class="abs shirt-photo" style="top:321px" role="img" aria-label="Photo of a white t-shirt with the store name printed on the chest"></div>
    <div class="abs package package--yellow" style="top:319px">
      • 2 Shirt choice<br>• 2 Design<br>• 3 Color<br>Sell: 1-25 earn 15%<br>25-50 earn 20%<br>50-100 earn 25%
    </div>

    <div class="abs shirt-photo" style="top:450px" role="img" aria-label="Photo of a white t-shirt with the store name printed on the chest"></div>
    <div class="abs package package--black" style="top:449px">
      • 4 Shirt choice<br>• 3 Design<br>• Unlimit color<br>Sell: 1-25 earn 10%<br>25-50 earn 15%<br>50-100 earn 20%
    </div>

    <div class="abs dots" style="left:-2px;top:563px;grid-template-columns:repeat(7,14px)">
      <span></span><span></span><span></span><span></span><span></span><span></span><span></span>
      <span></span><span></span><span></span><span></span><span></span><span></span><span></span>
      <span></span><span></span><span></span><span></span><span></span><span></span><span></span>
    </div>

    <svg class="abs" style="left:0;top:0" width="506" height="716" viewBox="0 0 506 716" aria-hidden="true">
      <path fill="var(--yellow)" d="M202,716 C240,640 330,590 420,590 C460,590 495,605 506,617 L506,716 Z"/>
      <path fill="var(--red)" d="M0,622 C60,598 175,606 227,716 L0,716 Z"/>
    </svg>

    <h2 class="abs contact-title">CONTACT US NOW</h2>
    <p class="abs contact-body">To build your free store to earn money for you organizaiotn or group! Call for more info!</p>

    <p class="abs phone">555-0192048</p>
    <p class="abs contact-line" style="top:662px">
      <svg width="18" height="18" viewBox="0 0 18 18" aria-hidden="true"><g fill="none" stroke="var(--black)" stroke-width="1.4"><circle cx="9" cy="9" r="8"/><ellipse cx="9" cy="9" rx="3.5" ry="8"/><line x1="1" y1="9" x2="17" y2="9"/><line x1="2.5" y1="5" x2="15.5" y2="5"/><line x1="2.5" y1="13" x2="15.5" y2="13"/></g></svg>
      www.shirtsatbrim.com
    </p>
    <p class="abs contact-line" style="top:684px">
      <svg width="18" height="13" viewBox="0 0 18 13" aria-hidden="true"><rect x=".7" y=".7" width="16.6" height="11.6" fill="none" stroke="var(--black)" stroke-width="1.4"/><polyline points=".7,.7 9,7.5 17.3,.7" fill="none" stroke="var(--black)" stroke-width="1.4"/></svg>
      shop@shirtsatbrim.com
    </p>
  </section>

  <section class="page page--back" aria-label="Back of fundraiser flyer">
    <svg class="abs" style="left:0;top:0" width="511" height="721" viewBox="0 0 511 721" aria-hidden="true">
      <circle cx="12" cy="18" r="89" fill="var(--red)"/>
      <path d="M460,96 A75,75 0 0 1 535,21" fill="none" stroke="var(--red)" stroke-width="11"/>
      <path d="M53,327 A58,58 0 0 1 -5,385" fill="none" stroke="var(--red)" stroke-width="11"/>
      <circle cx="527" cy="474" r="67" fill="var(--yellow)"/>
      <circle cx="6" cy="602" r="46" fill="var(--black)"/>
    </svg>

    <h2 class="abs benefits-title">BENEFITS</h2>

    <div class="abs dots" style="left:392px;top:97px;grid-template-columns:repeat(3,14px)">
      <span></span><span></span><span></span><span></span><span></span><span></span><span></span><span></span><span></span>
      <span></span><span></span><span></span><span></span><span></span><span></span><span></span><span></span><span></span>
      <span></span><span></span><span></span><span></span><span></span><span></span><span></span><span></span><span></span>
    </div>

    <ul class="abs benefit-list">
      <li>• No stock</li>
      <li>• No upfront cost</li>
      <li>• No order form</li>
      <li>• Instant order notification</li>
      <li>• Daily order sumary</li>
      <li>• No money exchange/collecting</li>
      <li>• No customer contact (covid approved)</li>
      <li>• No risk</li>
      <li>• No headaches</li>
      <li>• Tshirs are easy sale for the right purpose</li>
      <li>• Invest less time with sales and more time connecting with your audience to invest in a worthy cause</li>
      <li>• All fullfillment and shipping handled by Shirts At Brim</li>
      <li>• Online platform</li>
      <li>• Gain revenue for your organiztion</li>
    </ul>

    <div class="abs dots" style="left:100px;top:366px;grid-template-columns:repeat(9,14px)">
      <span></span><span></span><span></span><span></span><span></span><span></span><span></span><span></span><span></span>
      <span></span><span></span><span></span><span></span><span></span><span></span><span></span><span></span><span></span>
      <span></span><span></span><span></span><span></span><span></span><span></span><span></span><span></span><span></span>
    </div>

    <div class="abs brand brand--back"><span class="brand__dot"></span>SHIRTS AT BRIM</div>

    <svg class="abs" style="left:0;top:0" width="511" height="721" viewBox="0 0 511 721" aria-hidden="true">
      <polygon points="121,470 163,470 121,510" fill="var(--yellow)"/>
      <polygon points="390,636 390,676 350,676" fill="var(--red)"/>
    </svg>
    <div class="abs promise">
      <p class="promise__line promise__line--outline" style="top:5px">WIN WIN</p>
      <p class="promise__line promise__line--red" style="top:43px">SITUATION</p>
      <p class="promise__line promise__line--outline" style="top:77px">YOU CAN'T</p>
      <p class="promise__line promise__line--big" style="top:100px">LOSE</p>
    </div>
  </section>

</main>
</body>
</html>
```